Upmarket substance abuse facility needs trifold brochure

New private 16 bed residential substance abuse treatment facility in Mapleton, UT. Facility located in elegant 11,000 home with stunning views of the mountains. Facility is Tudor style with traditional furnishings-an aerial picture of facility is attached.

Attached are the logo, original art drafts, picture of facility and business card. Additional pictures of grounds will be attached later. Professional pictures are being taken on 12-12 and will be uploaded on 12-13 or 14.

The brochure is to emphasis the lovely home and park like grounds that sits at the base of a beautiful mountain range in Mapleton, UT. Focus is on treatment in serene and elegant location. Do not want colors too dark and the style of the maple leaf cannot be changed. Will need space for main picture of house on front, facility description, address and how to contact, treatment philosophy, treatment provided, Admission Criteria, and insurance information.

Do not have the contact information too small or written over a dark color. No solid colored backgrounds.

Overall theme should follow logo and business cards and stay more traditional with use of nature via maple leaf and mountain on logo.
The sample I am using is 8 1/2 tall by 11inches wide. The style is a roll style (folded in thirds). This smaller size can fit in an envelope.

Pages- 3 printed sides in front, 3 in back.

I attached one of the pictures, the picture of the facility from above. The rest of the pictures are being taken on this coming Wed and will be ready on Thursday. I will attach them to the brief then.

We are working on content and hope to have a draft on line later today. The general categories will be:

1. Front page: logo with name- picture of facility from above, descriptor- Residential Substance Dependence Treatment
2. First inside page: List of symptoms and problem behaviors we treat
3.Middle inside page: Intro to facility- first paragraph-what we provide and a second paragraph on treatment philosophy.
4.Third inside page: Services Provided
5. 3rd outside page (fold inside trifold): The Journey Quote
6. Payment options and address and phone at bottom

Note* for some reason the Look and Feel slider keeps reseting to neutral each time. Look at my posting for business cards and logo to see my scales. Also, the color choices offered in the brief are limited. Please use the gold and darker green, not the lighter green shown.

I just added more information to my brief on trifold style and category headings.

Thank You and I appreciate your hard work on our behalf,

Ruth

I just attached the draft of the text today to go along with the prior posting of he categories. 

I just answered all the questions that came in yesterday regarding text, photos, brochures size and time frames. I also just uploaded a word file with the text for the quote that I forgot to add the first time. 

Good Morning,

Just wanted to provide an update that all the designs are underconsideration by the owner. We will narrow it down once I recieve his feedback later this weekend.  

Thanks for your patience.

Ruth

I just uploaded the professional photographs today. I am still trying to decrease the file size of the arial shot of the facility as it will not upload.

The edited text document was uploaded today.  The items with lines through them should be eliminated.  The items highlighted in yellow are changes and new working.

Thanks.

Target Market(s)

Adults age 18 and over who struggle with substance abuse for alcohol and other substances. Also their families, therapists, medical professionals and insurance companies.

Industry/Entity Type

Residential

Font styles to use
Script
Other font styles liked:
• black chancery for headings

Requirements
Must have
• Same logo
Room for content categories of: treatment provided and philosophy, facility description, admission criteria, insurance/payment and contact information.

Trifold style
Logo and name at the top
Use colors in logo, but they do not have to be used in the same proportions.
Needs to feel comfortable, inviting and gracious.
Nice to have
• more white space and pictures than text space.
Should not have
• Do not use scrolls or other "feminine" embellishments other than the font used in the name/logo.
No solid color backgrounds for entire pages or large sections
Cannot change the maple leaf design
Few if any changes to the mountain depicted if used.

```html
<!DOCTYPE html>
<html lang="en">
<head>
<meta charset="utf-8">
<title>Aspen Ridge Recovery – Inside Panels</title>
<link rel="stylesheet" href="https://fonts.googleapis.com/css2?family=Fondamento&family=Crimson+Text:wght@400;600&display=swap">
<style>
  :root {
    --green: #2f6b2a;
    --green-dark: #245a20;
    --ink: #2b2b2b;
    --rule: #cfcfcf;
    --paper: #ffffff;
  }
  * { box-sizing: border-box; margin: 0; padding: 0; }
  html, body { width: 1200px; height: 927px; overflow: hidden; background: var(--paper); }
  .sheet {
    position: relative; width: 1200px; height: 927px; overflow: hidden;
    background: var(--paper);
    font-family: "Crimson Text", Georgia, serif; color: var(--ink);
  }
  .top-band { position: absolute; left: 0; top: 0; width: 1200px; height: 10px; background: var(--green); }
  .bottom-band { position: absolute; left: 0; top: 895px; width: 1200px; height: 32px; background: var(--green-dark); }
  .fold { position: absolute; top: 10px; width: 1px; height: 885px; background: var(--rule); }
  .fold--one { left: 400px; }
  .fold--two { left: 800px; }

  .panel { position: absolute; top: 10px; width: 400px; height: 885px; }
  .panel--left { left: 0; }
  .panel--middle { left: 400px; }
  .panel--right { left: 800px; }

  .heading {
    position: absolute; top: 18px; left: 0; width: 400px;
    display: flex; justify-content: center; align-items: center; gap: 10px;
    font-family: "Fondamento", "Times New Roman", serif; font-weight: 400;
    font-size: 17px; color: var(--green);
  }
  .heading svg { width: 44px; height: 12px; }

  .copy { position: absolute; font-size: 13.8px; line-height: 19px; text-align: justify; }
  .list { list-style: none; position: absolute; font-size: 13.8px; line-height: 19px; }
  .list li { position: relative; padding-left: 14px; margin-bottom: 4px; }
  .list li::before {
    content: ""; position: absolute; left: 1px; top: 8px; width: 4px; height: 4px;
    border-radius: 50%; background: var(--green);
  }
  .list .sub { padding-left: 28px; }
  .list .sub::before { left: 15px; }

  .photo { position: absolute; border: 3px solid var(--green); padding: 5px; background: var(--paper); }
  .photo > div { width: 100%; height: 100%; }
  .photo--hall { left: 30px; top: 427px; width: 346px; height: 379px; }
  .photo--hall > div { background: linear-gradient(180deg, #d9c6a4 0%, #a86b3a 45%, #5b3a24 100%); }
  .photo--entry { left: 428px; top: 58px; width: 346px; height: 367px; }
  .photo--entry > div { background: linear-gradient(180deg, #7a3d1f 0%, #9a5a2c 50%, #4a3428 100%); }
  .photo--theatre { left: 428px; top: 618px; width: 346px; height: 188px; }
  .photo--theatre > div { background: linear-gradient(180deg, #8a5a35 0%, #7a2e22 60%, #5e1f18 100%); }
  .photo--dining { left: 827px; top: 530px; width: 347px; height: 276px; }
  .photo--dining > div { background: linear-gradient(180deg, #e8dcc2 0%, #9c6232 55%, #6b3a1e 100%); }
</style>
</head>
<body>
<div class="sheet">
  <div class="top-band"></div>
  <div class="fold fold--one"></div>
  <div class="fold fold--two"></div>

  <section class="panel panel--left">
    <h2 class="heading">
      <svg viewBox="0 0 44 12"><path d="M2 4 Q18 12 42 6" fill="none" stroke="currentColor" stroke-width="1.3"/></svg>
      Symptoms Treated
      <svg viewBox="0 0 44 12"><path d="M2 6 Q26 12 42 4" fill="none" stroke="currentColor" stroke-width="1.3"/></svg>
    </h2>
    <p class="copy" style="left:30px; top:56px; width:346px;">The negative effects of substance dependence can be devastating for families and individuals alike. The impacts of addictions have far reaching consequences on health, career, self-esteem, finances, legal issues and relationships. If you or a loved one is struggling with the issues listed, we are here to help.</p>
    <ul class="list" style="left:30px; top:172px; width:346px;">
      <li>Significant relationship issues as a result of using</li>
      <li>Inability to keep financial obligations as a result of addiction</li>
      <li>Poor health, poor sleep, weight gain / loss, weakness, nausea, low energy</li>
      <li>Putting lives of self and others at risk.</li>
      <li>Employment and school struggles</li>
      <li>Unable to stop using or limiting drug / addiction use despite attempts to stop</li>
      <li>Low self esteem, anxiety, guilt and depression</li>
      <li>Hiding addiction and/or the amount used</li>
      <li>Stealing to pay for drug of choice</li>
    </ul>
  </section>

  <section class="panel panel--middle">
    <h2 class="heading">
      <svg viewBox="0 0 44 12"><path d="M2 4 Q18 12 42 6" fill="none" stroke="currentColor" stroke-width="1.3"/></svg>
      Facility
      <svg viewBox="0 0 44 12"><path d="M2 6 Q26 12 42 4" fill="none" stroke="currentColor" stroke-width="1.3"/></svg>
    </h2>
    <p class="copy" style="left:28px; top:466px; width:346px;">Aspen Ridge Recovery offers full spectrum addictions treatment. Services are provided for men and women 18 years of age or over with a primary diagnosis of substance dependence. Clients are also accepted who have a secondary mental health diagnosis (i.e. dual diagnosis). All potential clients are pre-screened for appropriateness prior to admission.</p>
  </section>

  <section class="panel panel--right">
    <h2 class="heading">
      <svg viewBox="0 0 44 12"><path d="M2 4 Q18 12 42 6" fill="none" stroke="currentColor" stroke-width="1.3"/></svg>
      Services Provided
      <svg viewBox="0 0 44 12"><path d="M2 6 Q26 12 42 4" fill="none" stroke="currentColor" stroke-width="1.3"/></svg>
    </h2>
    <p class="copy" style="left:27px; top:59px; width:346px;">Resident healing is anchored through services provided by seasoned leaders in the addiction field. Providers include Addictionologists, Masters level therapists, Advanced Substance Use Disorders Counselors, Dieticians, Physicians, Experiential Therapists in addition to other healing arts staff. Services include but are not limed to:</p>
    <ul class="list" style="left:27px; top:176px; width:346px;">
      <li>Daily group therapy</li>
      <li>Individual therapy twice weekly</li>
      <li>Case Management weekly</li>
      <li>Regular 12-step meeting participation</li>
      <li>Weekly aftercare follow-up groups at no additional charge for one year</li>
      <li>Intensive Outpatient Group Therapy</li>
      <li>ADA equipped bedroom &amp; bath</li>
      <li>Dietary Consults</li>
      <li>Physician Consults</li>
      <li>Experiential &amp; Recreational Therapies include:</li>
      <li class="sub">Equine</li>
      <li class="sub">Low-ropes</li>
      <li class="sub">Yoga</li>
      <li class="sub">Exercise- on site gym, nature walks, hiking, gardening</li>
    </ul>
  </section>

  <div class="photo photo--hall"><div role="img" aria-label="Two-storey great room with wood gallery, fireplace and rug"></div></div>
  <div class="photo photo--entry"><div role="img" aria-label="Wood-panelled entry hall with rug and two small trees"></div></div>
  <div class="photo photo--theatre"><div role="img" aria-label="Home theatre room with screen and leather seating"></div></div>
  <div class="photo photo--dining"><div role="img" aria-label="Dining room with long wood table, chandelier and bay windows"></div></div>

  <div class="bottom-band"></div>
</div>
</body>
</html>
```